Willowmere Counseling (Endure - Mend - Flourish) - Double Sided Business Card

I would like a 2-sided business card. Front: Matte Black or Navy with Logo & Tagline. Back: Name, Address, Phone Number, Email, & Website (maybe would like to include a small map pin-pointing location); Prefer front to be a gold/silver foil (iridescent); Back prefer white or light colored background with lettering that is easy to read and simple

Target Market(s)

Individuals & Couples (13 y.o. - ALL Adults); High end clientele

Industry/Entity Type

Licensed Professional Counselor (Mental Health)

Contact Information for Business Card

Name: Willowmere Counseling; Tagline: Endure - Mend - Flourish; Address: 3870 N. Garrick Ave., Suite 214, Fort Worth, TX 76132; Phone: (214) 555-0187; Website: www.WillowmereCounseling.example

Font styles to use
Serif

Requirements
Must have
• Logo on Front (Large) prefer gold/silver foil on a matte dark color (i.e. black, navy, etc.); Back of Card: All other relevant information

```html
<!DOCTYPE html>
<html lang="en">
<head>
<meta charset="utf-8">
<title>Willowmere Counseling – Business Card</title>
<link href="https://fonts.googleapis.com/css2?family=Cinzel:wght@500&family=Oswald:wght@600&family=Open+Sans:wght@400&display=swap" rel="stylesheet">
<style>
  :root {
    --backdrop: #d4d6d8;
    --card-dark: #2c2b2a;
    --card-light: #ffffff;
    --gold: #d7b23f;
    --silver: #b9bbbe;
    --ink: #141414;
    --ink-soft: #2a2a2a;
  }
  * { margin: 0; padding: 0; box-sizing: border-box; }
  html, body { width: 1200px; height: 800px; overflow: hidden; }
  body {
    background: var(--backdrop);
    display: flex;
    flex-direction: column;
    align-items: center;
    justify-content: center;
    gap: 30px;
  }
  .card {
    width: 630px;
    height: 360px;
    position: relative;
    box-shadow: 0 6px 18px rgba(0,0,0,0.18);
  }

  /* Front */
  .card-front {
    background: var(--card-dark);
    display: flex;
    flex-direction: column;
    align-items: center;
    justify-content: center;
  }
  .brand-mark {
    width: 64px;
    height: 64px;
    border: 3px solid var(--gold);
    border-radius: 50%;
    margin-bottom: 18px;
  }
  .brand-name {
    font-family: "Cinzel", serif;
    font-weight: 500;
    color: var(--gold);
    font-size: 40px;
    line-height: 1.05;
    letter-spacing: 2px;
    text-align: center;
  }
  .brand-rule {
    width: 380px;
    height: 2px;
    background: var(--silver);
    margin: 14px 0 10px;
  }
  .brand-tagline {
    font-family: "Cinzel", serif;
    font-weight: 500;
    color: var(--gold);
    font-size: 15px;
    letter-spacing: 2px;
  }

  /* Back */
  .card-back {
    background: var(--card-light);
    padding: 92px 40px 0 40px;
  }
  .contact-row {
    display: flex;
    align-items: flex-start;
  }
  .person {
    text-align: right;
    width: 225px;
    padding-right: 16px;
  }
  .person-name {
    font-family: "Oswald", sans-serif;
    font-weight: 600;
    font-size: 27px;
    color: var(--ink);
    line-height: 1.1;
  }
  .person-title {
    font-family: "Open Sans", sans-serif;
    font-size: 15px;
    color: var(--ink-soft);
  }
  .divider {
    width: 2px;
    height: 62px;
    background: var(--ink);
    margin-top: 6px;
  }
  .contact-list {
    list-style: none;
    padding-left: 12px;
    padding-top: 8px;
    font-family: "Open Sans", sans-serif;
    font-size: 15px;
    color: var(--ink);
    line-height: 1.45;
  }
  .contact-list li { display: flex; align-items: center; gap: 7px; }
  .contact-list svg { width: 13px; height: 13px; flex: none; }
  .address {
    font-family: "Open Sans", sans-serif;
    font-size: 16px;
    color: var(--ink);
    margin-top: 44px;
    padding-left: 20px;
  }
</style>
</head>
<body>
  <section class="card card-front">
    <div class="brand-mark"></div>
    <h1 class="brand-name">WILLOWMERE<br>COUNSELING</h1>
    <div class="brand-rule"></div>
    <p class="brand-tagline">ENDURE - MEND - FLOURISH</p>
  </section>

  <section class="card card-back">
    <div class="contact-row">
      <div class="person">
        <h2 class="person-name">Daniel Whitaker</h2>
        <p class="person-title">President</p>
      </div>
      <div class="divider"></div>
      <ul class="contact-list">
        <li>
          <svg viewBox="0 0 16 16" aria-hidden="true"><path d="M3 1.5l3 3-1.6 1.8a9 9 0 0 0 5.3 5.3L11.5 10l3 3-2 2C6.5 15 1 9.5 1 3.5z" fill="var(--ink)"/></svg>
          (214) 555-0187
        </li>
        <li>
          <svg viewBox="0 0 16 16" aria-hidden="true"><rect x="1" y="3" width="14" height="10" fill="none" stroke="var(--ink)" stroke-width="1.6"/><path d="M1 3l7 6 7-6" fill="none" stroke="var(--ink)" stroke-width="1.6"/></svg>
          daniel@WillowmereCounseling.example
        </li>
        <li>
          <svg viewBox="0 0 16 16" aria-hidden="true"><circle cx="8" cy="8" r="6.5" fill="none" stroke="var(--ink)" stroke-width="1.3"/><ellipse cx="8" cy="8" rx="3" ry="6.5" fill="none" stroke="var(--ink)" stroke-width="1.1"/><path d="M1.5 8h13M2.5 5h11M2.5 11h11" stroke="var(--ink)" stroke-width="1"/></svg>
          www.WillowmereCounseling.example
        </li>
      </ul>
    </div>
    <p class="address">3870 N. Garrick Ave., Suite 214, Fort Worth, TX 76132</p>
  </section>
</body>
</html>
```